Dental Specialist Needs a Business Card

We are a state of the art dental specialty office and need a business card that looks modern but professional.
I have provided our logo design in both vertical and horizontal. We use the design on letterhead in the vertical format but provided both forms for you. Thanks

Please add the address, phone and fax numbers I listed to all designs and please leave a space for website and for my employee name on each design. Thanks 2847 Halloway Avenue, Suite K East Marlow, NY 14391 Phone (716)382-9157 Fax:(716)382-9150 My name is Miles R.Dunford,D.D.S. If you want to show it with my name but the design needs to allow for the name to be switched.

Industry/Entity Type

Business

```html
<!DOCTYPE html>
<html lang="en">
<head>
<meta charset="utf-8">
<title>Northgate Endodontics P.C. — Business Card</title>
<link href="https://fonts.googleapis.com/css2?family=Inter:wght@300&family=Open+Sans:wght@400&display=swap" rel="stylesheet">
<style>
  :root {
    --paper: #ffffff;
    --ink: #111111;
    --sky: #00aaf5;
    --leaf: #8bc63f;
    --on-band: #ffffff;
  }
  * { margin: 0; padding: 0; box-sizing: border-box; }
  html, body { width: 1200px; height: 741px; overflow: hidden; background: var(--paper); }
  .card {
    position: relative;
    width: 1200px;
    height: 741px;
    background: var(--paper);
    font-family: "Inter", Helvetica, Arial, sans-serif;
  }
  .brand {
    position: absolute;
    top: 105px;
    left: 0;
    width: 1200px;
    display: flex;
    align-items: center;
    justify-content: center;
    gap: 30px;
  }
  .brand-dot {
    width: 96px;
    height: 96px;
    border-radius: 50%;
    background: var(--sky);
  }
  .brand-name {
    font-family: "Open Sans", Arial, sans-serif;
    font-weight: 400;
    font-size: 50px;
    color: var(--ink);
    letter-spacing: 0.5px;
  }
  .doctor-name {
    position: absolute;
    top: 386px;
    left: 0;
    width: 1200px;
    text-align: center;
    font-weight: 300;
    font-size: 67px;
    line-height: 1;
    color: var(--ink);
    letter-spacing: -0.5px;
  }
  .contact-band {
    position: absolute;
    top: 541px;
    left: 0;
    width: 1200px;
    height: 200px;
    display: flex;
  }
  .contact-phone {
    width: 603px;
    background: var(--sky);
    position: relative;
  }
  .contact-address {
    flex: 1;
    background: var(--leaf);
    position: relative;
  }
  .contact-icon { position: absolute; fill: var(--on-band); }
  .icon-phone { left: 54px; top: 54px; width: 62px; height: 52px; }
  .icon-pin { left: 641px; top: 56px; width: 42px; height: 68px; }
  .icon-pin { left: 38px; }
  .contact-lines {
    position: absolute;
    color: var(--on-band);
    font-weight: 300;
    font-size: 32px;
    line-height: 54px;
    white-space: nowrap;
  }
  .contact-phone .contact-lines { left: 138px; top: 49px; }
  .contact-address .contact-lines { left: 97px; top: 47px; }
</style>
</head>
<body>
  <div class="card">
    <div class="brand">
      <div class="brand-dot"></div>
      <div class="brand-name">Northgate Endodontics P.C.</div>
    </div>

    <div class="doctor-name">Miles R. Dunford D.D.S.</div>

    <div class="contact-band">
      <div class="contact-phone">
        <svg class="contact-icon icon-phone" viewBox="0 0 62 52" aria-hidden="true">
          <path d="M4 14 C4 4 58 4 58 14 L58 20 L45 20 L45 13 L17 13 L17 20 L4 20 Z"/>
          <path d="M20 16 L42 16 L54 36 L54 50 L8 50 L8 36 Z"/>
          <circle cx="31" cy="33" r="7" fill="#00aaf5"/>
          <circle cx="31" cy="33" r="3"/>
        </svg>
        <div class="contact-lines">
          <div>(716) 382-9157</div>
          <div>(716) 382-9150</div>
        </div>
      </div>
      <div class="contact-address">
        <svg class="contact-icon icon-pin" viewBox="0 0 42 68" aria-hidden="true">
          <path d="M21 0 C9.4 0 0 9.4 0 21 C0 36 21 68 21 68 C21 68 42 36 42 21 C42 9.4 32.6 0 21 0 Z"/>
          <circle cx="21" cy="20" r="7.5" fill="#8bc63f"/>
        </svg>
        <div class="contact-lines">
          <div>2847 Halloway Avenue, Suite K,</div>
          <div>East Marlow, NY 14391</div>
        </div>
      </div>
    </div>
  </div>
</body>
</html>
```